Design a van wrap

We require a full van wrap design for a construction and development company. The design must present a premium, professional, and highly visible brand image suitable for a modern construction business. See attached existing wrap. Require a whole new look.
Vehicle Details
- Vehicle: Velbro electric van (T7 / similar size)
- Wrap type: Full wrap (bonnet, sides, rear)
- Use Palmet image on the rear doors
Dimension uCarrio 8 L1H1 uCarrio 8 L2H1
Overall length ~4,800 mm ~5,250 mm
Overall width (excl. mirrors) ~1,874 mm ~1,874 mm
Overall height (H1) ~1,960 mm ~1,960 mm
Wheelbase ~3,100 mm ~3,450 mm
Roof height H1 (standard) H1 (standard)
Branding
- Company Name: KORVELT
- Industry: Construction & Development
- 4 bullets on each side of van detailing scope of business
- New Builds
- Basement Works
- Piling Works
- Demolition
- Engineering
- RC Frame Works
- Loft Conversions
- Refurbishment
Brand Style: Modern, strong, premium, clean
- Colours:
- Primary: Black and Brown
- Accent: Cream (for contrast and legibility if required - see business card)
- Existing assets: Logo will be provided (vector format)
Design Style & Finish
- Contemporary and bold
- Strong contrast for roadside visibility
- Suitable for commercial vinyl printing
- Avoid over-complication or excessive textures
Deliverables
- Print-ready files
- Vector format preferred (AI / EPS / PDF)
- High-resolution mockups showing all sides of the van
- Colour codes specified (CMYK / Pantone if applicable)
Target Outcome
A van wrap that clearly communicates professionalism, scale, and trust, stands out on the road, and reinforces a premium construction brand.

```html
<!DOCTYPE html>
<html lang="en">
<head>
<meta charset="utf-8">
<title>KORVELT Van Wrap</title>
<link rel="stylesheet" href="https://fonts.googleapis.com/css2?family=Jost:wght@500;600&display=swap">
<style>
  :root {
    --bg: #e8e8e8;
    --brown: #5a3f2e;
    --brown-dark: #4a3324;
    --black: #1c1c1c;
    --cream: #ece2cc;
    --tyre: #161616;
    --hub: #9a9a9a;
    --glass: #2a2a2a;
  }
  html, body {
    margin: 0;
    width: 1200px;
    height: 1200px;
    overflow: hidden;
    background: var(--bg);
  }
  .canvas {
    position: relative;
    width: 1200px;
    height: 1200px;
    font-family: "Jost", sans-serif;
  }
  .wrap-side {
    position: absolute;
    left: 50px;
    top: 110px;
    width: 1100px;
    height: 480px;
  }
  .wrap-rear {
    position: absolute;
    left: 340px;
    top: 660px;
    width: 520px;
    height: 460px;
  }
  .brand-name { font-weight: 600; fill: var(--cream); letter-spacing: 1px; }
  .service { font-weight: 500; fill: var(--cream); font-size: 15px; letter-spacing: 0.5px; }
  .contact-phone { font-weight: 600; fill: var(--cream); font-size: 36px; letter-spacing: 1px; }
  .contact-web { font-weight: 600; fill: var(--cream); font-size: 27px; letter-spacing: 0.5px; }
</style>
</head>
<body>
<div class="canvas">

  <svg class="wrap-side" viewBox="0 0 1100 480" aria-label="KORVELT van wrap, side panel">
    <path class="body-panel" d="M40 410 L40 270 Q44 225 100 205 L200 185 L290 95 Q305 70 340 68 L1060 55 Q1080 55 1080 75 L1080 410 Z" fill="var(--brown)"/>
    <path class="roof-band" d="M640 60 L1060 55 Q1080 55 1080 75 L1080 110 L600 110 Z" fill="var(--black)"/>
    <polygon class="service-band" points="300,205 365,115 1080,115 1080,410 960,410 900,290 365,290" fill="var(--black)"/>
    <polyline class="band-trim" points="1080,108 360,108 292,205 360,297 895,297 955,410" fill="none" stroke="var(--cream)" stroke-width="5"/>
    <polyline class="roof-trim" points="600,108 650,60" fill="none" stroke="var(--cream)" stroke-width="5"/>
    <path class="cab-window" d="M175 205 L285 110 L305 110 L305 205 Z" fill="var(--glass)"/>
    <polygon class="front-stripe" points="40,280 95,272 150,410 110,410" fill="var(--cream)"/>
    <polygon class="front-stripe" points="112,270 132,268 185,410 168,410" fill="var(--cream)"/>
    <polygon class="door-stripe" points="318,325 335,325 380,410 362,410" fill="var(--cream)"/>
    <rect class="skirt" x="40" y="395" width="1040" height="22" fill="var(--black)"/>
    <circle cx="210" cy="412" r="60" fill="var(--tyre)"/>
    <circle cx="210" cy="412" r="30" fill="var(--hub)"/>
    <circle cx="900" cy="412" r="60" fill="var(--tyre)"/>
    <circle cx="900" cy="412" r="30" fill="var(--hub)"/>

    <rect class="brand-square" x="185" y="296" width="22" height="22" fill="var(--cream)"/>
    <text class="brand-name" x="185" y="342" font-size="22">KORVELT</text>

    <text class="brand-name" x="405" y="180" font-size="52">KORVELT</text>
    <text class="service" x="400" y="215">• NEW BUILDS</text>
    <text class="service" x="400" y="237">• DEMOLITION</text>
    <text class="service" x="400" y="259">• ENGINEERING</text>
    <text class="service" x="560" y="215">• BASEMENT WORKS</text>
    <text class="service" x="560" y="237">• ENGINEERING</text>
    <text class="service" x="560" y="259">• RC FRAME WORKS</text>
    <text class="service" x="745" y="215">• PILING WORKS</text>
    <text class="service" x="745" y="237">• LOFT CONVERSIONS</text>
    <text class="service" x="745" y="259">• REFURBISHMENT</text>

    <text class="contact-phone" x="400" y="345">08001 472 905</text>
    <text class="contact-web" x="400" y="382">WWW.KORVELT.CO.UK</text>
  </svg>

  <svg class="wrap-rear" viewBox="0 0 520 460" aria-label="KORVELT van wrap, rear doors">
    <defs>
      <linearGradient id="rear-image-tone" x1="0" y1="0" x2="0" y2="1">
        <stop offset="0" stop-color="#a9c3df"/>
        <stop offset="0.45" stop-color="#c98b63"/>
        <stop offset="1" stop-color="#8d8f93"/>
      </linearGradient>
    </defs>
    <path class="rear-doors" d="M30 30 Q30 10 55 10 L465 10 Q490 10 490 30 L490 410 L30 410 Z" fill="var(--brown)"/>
    <text class="brand-name" x="260" y="62" font-size="40" text-anchor="middle">KORVELT</text>
    <rect x="48" y="85" width="424" height="265" fill="url(#rear-image-tone)" role="img" aria-label="Photograph of a modern brick apartment building under a blue sky"/>
    <line class="door-split" x1="260" y1="85" x2="260" y2="350" stroke="var(--brown-dark)" stroke-width="3"/>
    <text class="contact-web" x="260" y="388" text-anchor="middle">WWW.KORVELT.CO.UK</text>
    <rect class="bumper" x="20" y="410" width="480" height="38" rx="6" fill="var(--black)"/>
  </svg>

</div>
</body>
</html>
```